American cannabis tech company business card design

Quillo.com is seeking a modern, professional, and brand-aligned business card that represents our company and its core values: Mission, Story, Values, and Impact. As an innovative cannabis company, we want a business card that is not only visually appealing but also serves as a representation of who we are and what we stand for.

Project Scope: Design a double-sided business card that integrates our brand identity and core values. Incorporate our key brand elements, ensuring a sleek and contemporary aesthetic. Visually reflect our core values (Mission, Story, Values, Impact) in a way that is engaging yet professional.

Target Market(s)

Vendors, third parties,

Contact Information for Business Card

Contact details (name, title, email, phone, website, etc.)

Font styles to use
Other font styles liked:
• Caslon, Centra

Colors

Designer to choose colors to be used in the design.

Requirements
Must have
• Quillo.com logo and branding A creative yet clean way to integrate our core values (Mission, Story, Values, Impact) Modern typography and a well-structured layout
Nice to have
• forest green, grey, white, black
Should not have
• references to marijuana, leafs, plants, or related product

```html
<!DOCTYPE html>
<html lang="en">
<head>
<meta charset="utf-8">
<title>Quillo.com Business Card</title>
<link href="https://fonts.googleapis.com/css2?family=Libre+Caslon+Text:wght@400;700&family=Arimo:wght@400&display=swap" rel="stylesheet">
<style>
  :root {
    --forest: #19341b;
    --paper: #ffffff;
    --cream: #fbfaf4;
    --cream-soft: #c9d3c4;
    --stage: #3a3a3a;
    --ink: #1b1b1b;
    --rule: #4d5f4e;
  }
  * { box-sizing: border-box; margin: 0; padding: 0; }
  html, body { width: 1200px; height: 689px; overflow: hidden; }
  body {
    background: var(--stage);
    font-family: "Libre Caslon Text", "Times New Roman", serif;
    position: relative;
  }
  .card {
    position: absolute;
    top: 194px;
    width: 520px;
    height: 300px;
    border-radius: 24px;
    overflow: hidden;
  }
  .card--front { left: 50px; background: var(--forest); }
  .card--back { left: 630px; background: var(--paper); }

  .wordmark {
    font-family: "Libre Caslon Text", "Times New Roman", serif;
    font-weight: 700;
    letter-spacing: 1px;
    line-height: 1;
  }
  .front-stack {
    position: absolute;
    left: 0; right: 0; top: 50%;
    transform: translateY(-50%);
    text-align: center;
  }
  .card--front .wordmark {
    font-size: 92px;
    color: var(--cream);
  }
  .values {
    list-style: none;
    display: flex;
    justify-content: center;
    gap: 14px;
    margin-top: 26px;
    font-family: "Arimo", Arial, sans-serif;
    font-size: 12px;
    letter-spacing: 3px;
    text-transform: uppercase;
    color: var(--cream-soft);
  }
  .values li + li::before {
    content: "";
    display: inline-block;
    width: 4px; height: 4px;
    border-radius: 50%;
    background: var(--cream-soft);
    vertical-align: middle;
    margin: -2px 14px 0 0;
  }
  .card--back .wordmark {
    position: absolute;
    left: 34px; top: 128px;
    font-size: 46px;
    color: var(--forest);
  }
  .divider {
    position: absolute;
    left: 252px; top: 48px;
    width: 1px; height: 204px;
    background: var(--rule);
  }
  .contact {
    position: absolute;
    left: 272px; top: 52px;
    right: 16px;
    color: var(--ink);
  }
  .contact__name {
    font-weight: 700;
    font-size: 19px;
    color: var(--forest);
  }
  .contact__title {
    font-family: "Arimo", Arial, sans-serif;
    font-size: 13px;
    margin: 6px 0 14px;
    color: #333;
  }
  .contact__list { list-style: none; }
  .contact__item {
    display: flex;
    align-items: center;
    gap: 10px;
    font-size: 13.5px;
    margin-bottom: 8px;
  }
  .contact__item svg { width: 14px; height: 14px; flex: none; fill: var(--forest); }
  .contact__address {
    font-size: 13.5px;
    line-height: 1.45;
    margin-top: 14px;
  }
</style>
</head>
<body>
  <section class="card card--front" aria-label="Card front">
    <div class="front-stack">
      <div class="wordmark">QUILLO</div>
      <ul class="values" aria-label="Core values">
        <li>Mission</li>
        <li>Story</li>
        <li>Values</li>
        <li>Impact</li>
      </ul>
    </div>
  </section>

  <section class="card card--back" aria-label="Card back">
    <div class="wordmark">QUILLO</div>
    <div class="divider"></div>
    <div class="contact">
      <p class="contact__name">Daniel Harper</p>
      <p class="contact__title">Owner</p>
      <ul class="contact__list">
        <li class="contact__item">
          <svg viewBox="0 0 24 24" aria-hidden="true"><path d="M6.6 10.8a15.1 15.1 0 0 0 6.6 6.6l2.2-2.2a1 1 0 0 1 1-.25 11.4 11.4 0 0 0 3.6.57 1 1 0 0 1 1 1V20a1 1 0 0 1-1 1A17 17 0 0 1 3 4a1 1 0 0 1 1-1h3.5a1 1 0 0 1 1 1c0 1.25.2 2.45.57 3.57a1 1 0 0 1-.25 1z"/></svg>
          044-555 218 604
        </li>
        <li class="contact__item">
          <svg viewBox="0 0 24 24" aria-hidden="true"><path d="M2 5h20v14H2z M2 5l10 8 10-8" fill="none" stroke="#19341b" stroke-width="2.4"/></svg>
          info@quillo.com
        </li>
        <li class="contact__item">
          <svg viewBox="0 0 24 24" aria-hidden="true"><circle cx="12" cy="12" r="9" fill="none" stroke="#19341b" stroke-width="2.4"/><path d="M3 12h18M12 3c3 3 3 15 0 18M12 3c-3 3-3 15 0 18" fill="none" stroke="#19341b" stroke-width="1.8"/></svg>
          www.quillo.com
        </li>
      </ul>
      <p class="contact__address">421, Address line goes here<br>45452, Country name</p>
    </div>
  </section>
</body>
</html>
```